I need business cards for a company that will be an umbrella for many retail stores. I need them to be sleek and modern. I would like some white and black in the background of the card as these are the office colours the logo is attached.
Target Market(s)
worldwide
Industry/Entity Type
Business
Requirements
Must have
- traditional business card shape
Should not have
- too many colours
no swirly text

```html
<!DOCTYPE html>
<html lang="en">
<head>
<meta charset="utf-8">
<title>Mira General Trading – Business Cards</title>
<link rel="stylesheet" href="https://fonts.googleapis.com/css2?family=PT+Sans:wght@400&display=swap">
<style>
  :root {
    --page-bg: #ffffff;
    --card-bg: #ffffff;
    --card-edge: #a9a9a9;
    --brand-blue: #0a5ea8;
    --soft-blue: #9bb8e0;
    --ink: #1f1f1f;
    --brand-ink: #2b4f7e;
    --icon-grey: #9a9a9a;
  }
  * { box-sizing: border-box; margin: 0; padding: 0; }
  html, body {
    width: 1200px;
    height: 900px;
    overflow: hidden;
    background: var(--page-bg);
  }
  .canvas {
    position: relative;
    width: 1200px;
    height: 900px;
    font-family: "PT Sans", sans-serif;
    color: var(--ink);
  }
  .card {
    position: absolute;
    background: var(--card-bg);
    border: 2px solid var(--card-edge);
    overflow: hidden;
  }
  .card--front { left: 32px; top: 8px; width: 768px; height: 422px; }
  .card--back  { left: 400px; top: 468px; width: 766px; height: 424px; }

  .brand-name {
    font-family: "PT Sans", sans-serif;
    font-weight: 400;
    color: var(--brand-ink);
    font-size: 26px;
    line-height: 1.15;
    letter-spacing: 1px;
  }
  .card--front .brand-name { position: absolute; left: 40px; top: 74px; }

  .name-tab {
    position: absolute;
    left: 388px; top: 168px;
    width: 380px; height: 84px;
    background: var(--soft-blue);
    border-radius: 22px 0 0 22px;
    padding: 14px 0 0 24px;
  }
  .person-name { font-size: 24px; line-height: 1.2; }
  .person-email { font-size: 19px; margin-top: 4px; }

  .contact-line {
    position: absolute;
    display: flex;
    align-items: center;
    gap: 10px;
    font-size: 19px;
  }
  .contact-icon { width: 30px; height: 30px; fill: var(--icon-grey); }

  .card--front .contact-line--phone   { left: 36px; top: 280px; }
  .card--front .contact-line--address { left: 36px; top: 320px; }

  .band { position: absolute; left: 0; top: 0; }

  .card--back .brand-name {
    position: absolute;
    left: 44px; top: 210px;
    transform: rotate(-90deg);
    transform-origin: left top;
    white-space: nowrap;
  }
  .card--back .brand-name span { display: block; }
  .back-details { position: absolute; left: 314px; top: 122px; }
  .card--back .contact-line { flex-direction: row; }
  .card--back .contact-line--phone   { right: 124px; top: 236px; }
  .card--back .contact-line--address { right: 124px; top: 274px; }
</style>
</head>
<body>
<main class="canvas">

  <section class="card card--front" aria-label="Business card front">
    <div class="brand-name">Mira<br>General Trading</div>

    <div class="name-tab">
      <p class="person-name">Your name</p>
      <p class="person-email">email@yourdomain.com</p>
    </div>

    <p class="contact-line contact-line--phone">
      <svg class="contact-icon" viewBox="0 0 30 30" aria-hidden="true">
        <path d="M17 3c-3 1-6 6-7 12-1 5 0 9 2 11l3-1c1 0 1-1 1-2l-2-4c-1-1-2 0-2-1 0-3 1-6 3-8 1-1 2 0 2-1l1-4c0-1-1-2-1-2z"/>
      </svg>
      Your telephone
    </p>
    <p class="contact-line contact-line--address">
      <svg class="contact-icon" viewBox="0 0 30 30" aria-hidden="true">
        <rect x="9" y="4" width="12" height="8"/>
        <rect x="3" y="13" width="24" height="10"/>
        <rect x="2" y="24" width="26" height="3"/>
      </svg>
      Your Address
    </p>
  </section>

  <section class="card card--back" aria-label="Business card back">
    <svg class="band" width="766" height="424" viewBox="0 0 766 424" aria-hidden="true">
      <polygon points="316,0 656,0 656,132 316,76" fill="var(--brand-blue)"/>
      <polygon points="316,336 656,388 656,424 316,424" fill="var(--brand-blue)"/>
    </svg>

    <div class="brand-name"><span>Mira</span><span>General Trading</span></div>

    <div class="back-details">
      <p class="person-name">Your name</p>
      <p class="person-email">email@yourdomain.com</p>
    </div>

    <p class="contact-line contact-line--phone">
      Your telephone
      <svg class="contact-icon" viewBox="0 0 30 30" aria-hidden="true">
        <path d="M17 3c-3 1-6 6-7 12-1 5 0 9 2 11l3-1c1 0 1-1 1-2l-2-4c-1-1-2 0-2-1 0-3 1-6 3-8 1-1 2 0 2-1l1-4c0-1-1-2-1-2z"/>
      </svg>
    </p>
    <p class="contact-line contact-line--address">
      Your Address
      <svg class="contact-icon" viewBox="0 0 30 30" aria-hidden="true">
        <rect x="9" y="4" width="12" height="8"/>
        <rect x="3" y="13" width="24" height="10"/>
        <rect x="2" y="24" width="26" height="3"/>
      </svg>
    </p>
  </section>

</main>
</body>
</html>
```